Pipe and Drape Company Web site

Name of client is "Harbor Linen" with a tagline of, "The Finest Linen, The Finest Care." which will need to go across the middle of the header area. Logo will be on the left. Connectors on the right. Connectors being, join newsletter, framebook, chirpster, worked Up, etc...

Please refer to www.velvetmonarchs.example for feel and layout and then www.northfieldhawks.example for background imagery style and preferred color scheme. Colors for the site should be black and dark purple with sub page text areas being white with black text. Yet still surrounded with black framing and purple infused background. We'll need a Large impactful main image area to display scrolling images. Below that will be 4 content area boxes with each of the following titles. "Corporate Events" , "Weddings" , "Special Events" , and "Products".

Main nav will need to be across the top of main image and include the 5 following tabs: "Harbor Experience", "DrapeRental" , "Gallery" , "Resources" ,
"Contact Us". Also leave a blank space on the right end of main nav in case we decide to add a 6th main nav at a later date.

This is a nationwide company and is a leader in their industry. The site should look very high end and classy. Highest quality and largest selection of drape anywhere. It should convey dependability, professionalism, Trustworthy, and expertise.

The main calls to action should be to get the visitor to call the phone number, or contact via email.

Main visitor demographic will be female event coordinators.

Sub Page design will vary based on the market segment chosen from home page. However, we feel the "wedding" category would be a good option since those pages might have a lighter look and feminine feel to them. Be sure to make it simple for the visitor to go back from the sub page, to the hame page via nav choices, or market segment boxes across the bottom again.

```html
<!DOCTYPE html>
<html lang="en">
<head>
<meta charset="utf-8">
<title>Harbor Linen – Pipe and Drape</title>
<link rel="stylesheet" href="https://fonts.googleapis.com/css2?family=Marcellus&family=Open+Sans:wght@400;600&family=Arimo:wght@400&display=swap">
<style>
  :root {
    --bg-deep: #2a0a45;
    --bg-mid: #4b1773;
    --bg-glow: #6a2a9a;
    --topbar: #22073a;
    --nav-top: #1b0a26;
    --nav-bottom: #000000;
    --frame-black: #000000;
    --title-purple: #5e0b80;
    --lavender: #c9a2ec;
    --nav-active: #c898f0;
    --white: #ffffff;
    --body-text: #2b0a52;
    --bullet: #8a5ab0;
  }
  * { margin: 0; padding: 0; box-sizing: border-box; }
  html, body { width: 1200px; height: 1010px; overflow: hidden; }
  body {
    position: relative;
    font-family: "Arimo", Arial, sans-serif;
    color: var(--white);
    background:
      radial-gradient(circle at 12% 30%, rgba(190,140,230,.35), transparent 22%),
      radial-gradient(circle at 92% 35%, rgba(170,110,220,.35), transparent 20%),
      radial-gradient(ellipse at 50% 40%, var(--bg-glow), var(--bg-mid) 45%, var(--bg-deep) 100%);
  }
  a { color: inherit; text-decoration: none; }

  .top-bar {
    position: absolute; left: 0; top: 0; width: 1200px; height: 42px;
    background: var(--topbar);
  }
  .connectors {
    position: absolute; right: 127px; top: 15px;
    font-size: 12px; display: flex; gap: 6px; align-items: center;
  }
  .connectors .newsletter { text-decoration: underline; }
  .social-names { display: flex; gap: 6px; font-size: 10px; color: var(--lavender); margin-left: 4px; }

  .brand-name {
    position: absolute; left: 118px; top: 80px; white-space: nowrap;
    font-family: "Marcellus", Georgia, serif; font-size: 44px; line-height: 1;
  }
  .tagline {
    position: absolute; left: 408px; top: 76px;
    font-family: "Marcellus", Georgia, serif; font-size: 24px; color: var(--lavender);
  }
  .header-contact { position: absolute; right: 128px; top: 64px; text-align: right; }
  .header-contact .phone { font-family: "Marcellus", Georgia, serif; font-size: 23px; }
  .header-contact .email { font-size: 12px; margin-top: 5px; }

  .main-nav {
    position: absolute; left: 116px; top: 139px; width: 960px; height: 51px;
    background: linear-gradient(var(--nav-top), var(--nav-bottom));
    display: flex; align-items: center; padding-left: 25px; gap: 21px;
    font-family: "Open Sans", Arial, sans-serif; font-size: 15px; text-transform: uppercase;
  }
  .main-nav .active { color: var(--nav-active); }

  .hero-frame {
    position: absolute; left: 116px; top: 190px; width: 960px; height: 483px;
    background: var(--white); padding: 13px;
  }
  .hero-image {
    width: 934px; height: 457px;
    background: linear-gradient(100deg, #d9b98a 0%, #c89a7a 30%, #8f5fc4 55%, #7c45b8 100%);
  }

  .segments {
    position: absolute; left: 117px; top: 689px; width: 962px; height: 244px;
    background: var(--frame-black);
  }
  .segment {
    position: absolute; top: 13px; width: 226px; height: 221px; background: var(--white);
  }
  .segment:nth-child(1) { left: 13px; }
  .segment:nth-child(2) { left: 250px; }
  .segment:nth-child(3) { left: 487px; }
  .segment:nth-child(4) { left: 723px; }
  .segment-title {
    height: 43px; background: var(--title-purple);
    font-family: "Marcellus", Georgia, serif; font-weight: 400; font-size: 24px;
    padding: 4px 0 0 7px; line-height: 34px;
  }
  .segment-image { height: 68px; }
  .segment:nth-child(1) .segment-image { background: linear-gradient(90deg, #6b4a3a, #b0806a, #5a3a2e); }
  .segment:nth-child(2) .segment-image { background: linear-gradient(90deg, #d9a97a, #f2ece6, #e8c9a2); }
  .segment:nth-child(3) .segment-image { background: linear-gradient(90deg, #c9c0a6, #eee8da, #c8bfa4); }
  .segment:nth-child(4) .segment-image { background: linear-gradient(90deg, #6a4a90, #e8e6ee, #5a3c84); }
  .segment-text {
    padding: 8px 10px 0 6px; font-size: 12px; line-height: 18px; letter-spacing: .2px; color: var(--body-text);
  }
  .segment-list { list-style: none; padding: 7px 0 0 12px; font-size: 12px; line-height: 22px; color: var(--body-text); }
  .segment-list li::before { content: "››"; color: var(--bullet); margin-right: 6px; font-size: 11px; }

  .footer-nav {
    position: absolute; left: 120px; top: 944px; display: flex; gap: 15px;
    font-size: 12px; color: #e6d4f5;
  }
  .footer-social {
    position: absolute; right: 122px; top: 946px; display: flex; gap: 6px; font-size: 10px; color: var(--lavender);
  }
  .footer-contact { position: absolute; left: 118px; top: 967px; display: flex; align-items: baseline; gap: 16px; }
  .footer-contact .phone { font-family: "Marcellus", Georgia, serif; font-size: 23px; }
  .footer-contact .email { font-size: 12px; }
  .copyright { position: absolute; right: 122px; top: 974px; font-size: 12px; }
</style>
</head>
<body>
  <div class="top-bar">
    <div class="connectors">
      <a class="newsletter" href="#">Join Newsletter</a>
      <span>| Join us on</span>
      <span class="social-names"><span>framebook</span><span>chirpster</span><span>worked Up</span><span>talkline</span></span>
    </div>
  </div>

  <header>
    <p class="brand-name">Harbor Linen</p>
    <p class="tagline">The Finest Linen, The Finest Care</p>
    <div class="header-contact">
      <p class="phone">Call us - 555 014 7890</p>
      <p class="email">email: contact@harborlinen.example</p>
    </div>
  </header>

  <nav class="main-nav">
    <a class="active" href="#">Home</a>
    <a href="#">Harbor Experience</a>
    <a href="#">DrapeRental</a>
    <a href="#">Gallery</a>
    <a href="#">Resources</a>
    <a href="#">Contact Us</a>
  </nav>

  <section class="hero-frame">
    <div class="hero-image" role="img" aria-label="Bride and groom holding a rose bouquet in front of purple pleated drape"></div>
  </section>

  <section class="segments">
    <article class="segment">
      <h2 class="segment-title">Corporate Events</h2>
      <div class="segment-image" role="img" aria-label="Group of guests celebrating at a corporate party"></div>
      <p class="segment-text">Lorem ipsum dolor sit amet, consectetur adipiscing elit. Curabitur ut mi velit. Aenean quis orci augue. Phasellus eget nibh eros. Cum sociis natoque penatibus</p>
    </article>
    <article class="segment">
      <h2 class="segment-title">Wedding</h2>
      <div class="segment-image" role="img" aria-label="Bride in white gown with scattered rose petals"></div>
      <p class="segment-text">Curabitur ut mi velit. Aenean quis orci augue. Phasellus eget nibh eros. Cum sociis natoque penatibus Lorem ipsum dolor sit amet, consectetur adipiscing elit.</p>
    </article>
    <article class="segment">
      <h2 class="segment-title">Special Events</h2>
      <div class="segment-image" role="img" aria-label="Banquet hall with cream drape and set tables"></div>
      <p class="segment-text">Lorem ipsum dolor sit amet, consectetur adipiscing elit. Curabitur ut mi velit. Aenean quis orci augue. Phasellus eget nibh eros. Cum sociis natoque penatibus</p>
    </article>
    <article class="segment">
      <h2 class="segment-title">Products</h2>
      <div class="segment-image" role="img" aria-label="Chairs with white covers and purple sashes"></div>
      <ul class="segment-list">
        <li>Lorem ipsum dolor sit</li>
        <li>Consectetur adipiscing</li>
        <li>Lorem ipsum</li>
        <li>Dolor sit amet,</li>
      </ul>
    </article>
  </section>

  <footer>
    <nav class="footer-nav">
      <a href="#">Home</a>
      <a href="#">Harbor Experience</a>
      <a href="#">DrapeRental</a>
      <a href="#">Gallery</a>
      <a href="#">Resources</a>
      <a href="#">Contact Us</a>
    </nav>
    <div class="footer-social"><span>framebook</span><span>chirpster</span><span>worked Up</span><span>talkline</span></div>
    <div class="footer-contact">
      <p class="phone">Call us - 555 014 7890</p>
      <p class="email">email: contact@harborlinen.example</p>
    </div>
    <p class="copyright">© 2011 Harborlinen . All rights reserved.</p>
  </footer>
</body>
</html>
```